Massage Clinic needs a Flyer for Advertising

Our massage clinic, 'Keel Street Remedial Therapy', has recently opened in Osborne Park, Western Australia. We are specialists in deep tissue and sports massage. We also offer relaxation, trigger point therapy, stretching techniques, and postural and functional movement analysis. We're based within the same building complex as a personal training and IronForge box. There are also a number of local gyms in the area. Our target clients are both the local athletes, but also local business (Osborne Park is a business district in Perth).

We need double-sided DL size flyer. We would like the design to incorporate the colouring of the logo (green, purple, grey), but happy for it to use anything that enhances this also. Logo has been attached (.png and .ai format). There is also a selection of photos available to use if required, other stylised images would also be accepted. We'd like the flyer to include business details, services, and price list (price list is optional). We can provide further descriptions of key therapies on offer if required for inclusion.

Target Market(s)

Local athletes (gym, IronForge, sport), and local business employees.

Industry/Entity Type

Massage Therapy

Font styles to use
Sans Serif

Requirements
Must have
• List of Services to be included:
• Relaxation Massage
• Deep Tissue Massage
• Sports Massage
• Neuromuscular (Trigger Point) Therapy
• Postural Analysis
• Musculoskeletal and Functional Movement Screening
• Therapeutic Stretching (including Proprioceptive Neuromuscular Facilitation and Muscle Energy Technique)
• All sessions are customised to suit the needs of the client, and may incorporate a variety of the above techniques.
• Business location and Contact details:
• 4/61 Tarrant Lane, Osborne Park WA 6017
• Phone: 0412 573 604
• Email: info@keelstreet.example.net
Nice to have
• Symbols for showing the company has Chatterly and Snapframe accounts.
• The business is also a member of NRTG - logo attached below, please include.
• Price details are shown in one of the attached images, and copied below:
• Individual -
• 30 minutes $45
• 60 minutes $85
• Packages -
• 4 x 30 minutes $165
• 4 x 60 minutes $305
• (Packages valid for two months; pre-payment required).
Should not have
• Please don't use any imagery/design that looks suited to a day-spa environment. My massage clinic is located within a gym environment.
• If you use stock photo's, please select one where the therapists hands are female (both are stuff are currently female therapists).

```html
<!DOCTYPE html>
<html lang="en">
<head>
<meta charset="utf-8">
<title>Keel Street Remedial Therapy – Flyer</title>
<link href="https://fonts.googleapis.com/css2?family=Didact+Gothic&family=Nunito+Sans:wght@600;700&display=swap" rel="stylesheet">
<style>
  :root {
    --bg-dark: #4d4d4e;
    --bg-mid: #616162;
    --band: #777778;
    --green: #8cc43f;
    --green-dark: #6f9e2e;
    --purple: #6b2d8f;
    --white: #ffffff;
    --ink: #2d2d2d;
    --light: #e2e2e2;
  }
  * { margin: 0; padding: 0; box-sizing: border-box; }
  html, body { width: 1200px; height: 2517px; overflow: hidden; }
  body {
    position: relative;
    font-family: "Didact Gothic", sans-serif;
    color: var(--white);
    background: linear-gradient(180deg, var(--bg-mid) 0%, var(--bg-dark) 45%, var(--bg-dark) 80%, var(--light) 88%, var(--white) 100%);
  }
  .hero { position: absolute; left: 0; top: 0; width: 1200px; height: 1060px; }

  .brand-seal {
    position: absolute; left: 630px; top: 579px; width: 486px; height: 486px;
    border-radius: 50%; background: var(--white);
    border: 12px solid var(--green-dark);
    display: flex; flex-direction: column; align-items: center; justify-content: center;
    text-align: center;
  }
  .brand-name {
    font-family: "Nunito Sans", sans-serif; font-weight: 600; color: var(--purple);
    font-size: 66px; line-height: 1.05;
  }
  .brand-name .sub { display: block; font-size: 40px; margin-top: 14px; }

  .services {
    position: absolute; left: 60px; top: 1060px; width: 960px; list-style: none;
  }
  .services li {
    position: relative; padding-left: 62px; font-size: 48px; line-height: 82px;
  }
  .services li::before {
    content: ""; position: absolute; left: 0; top: 30px; width: 28px; height: 28px;
    background: var(--white); clip-path: polygon(100% 0, 100% 100%, 0 100%);
  }
  .services .aside { font-size: 34px; }
  .services .wrap { line-height: 62px; padding-top: 10px; }
  .services .wrap::before { top: 30px; }
  .services .note { display: block; font-size: 36px; line-height: 50px; }

  .social {
    position: absolute; left: 1040px; top: 1452px; width: 175px; height: 293px;
    background: var(--white); border-radius: 22px 0 0 22px;
    display: flex; flex-direction: column; justify-content: space-around; align-items: center;
    padding: 18px 0;
  }
  .social-item { display: flex; flex-direction: column; align-items: center; gap: 8px; }
  .social-square { width: 80px; height: 80px; background: #5b7ec1; }
  .social-item:nth-child(2) .social-square { background: #4f6f96; }
  .social-label { font-size: 22px; color: var(--ink); }

  .custom-band {
    position: absolute; left: 0; top: 1816px; width: 1200px; height: 126px;
    background: var(--band); text-align: center; font-size: 33px; line-height: 46px;
    padding-top: 16px;
  }

  .price-box {
    position: absolute; top: 1984px; height: 332px; border-radius: 30px; overflow: hidden;
    box-shadow: 0 4px 10px rgba(0,0,0,.18);
  }
  .price-box.individual { left: 47px; width: 470px; }
  .price-box.packages { left: 577px; width: 564px; }
  .price-head {
    height: 92px; background: var(--white); color: var(--purple);
    font-family: "Nunito Sans", sans-serif; font-weight: 700; font-size: 40px;
    display: flex; align-items: center; justify-content: center;
  }
  .price-body { height: 240px; background: var(--green); padding: 0 30px; }
  .price-row {
    height: 120px; display: flex; align-items: baseline; justify-content: center;
    padding-top: 26px; font-size: 68px; white-space: nowrap;
  }
  .price-row + .price-row { border-top: 2px solid rgba(255,255,255,.55); }
  .price-row .unit { font-size: 52px; margin: 0 12px 0 10px; }
  .price-row .dash { font-size: 52px; margin-right: 12px; }
  .price-row .times { font-size: 40px; margin: 0 10px; }
  .price-row .cur { font-size: 52px; }

  .price-note {
    position: absolute; left: 600px; top: 2336px; width: 520px; text-align: center;
    color: var(--ink); font-size: 30px; line-height: 38px;
  }

  .contact {
    position: absolute; left: 590px; top: 2426px; width: 560px; text-align: center;
    color: var(--ink); font-size: 24px; line-height: 32px; list-style: none;
  }
  .contact strong { font-family: "Nunito Sans", sans-serif; font-weight: 700; color: var(--purple); }

  .member {
    position: absolute; left: 58px; top: 2341px; display: flex; align-items: center; gap: 26px;
  }
  .member-badge { width: 134px; height: 142px; background: #1d4f9c; border-radius: 10px; }
  .member-name {
    font-family: "Nunito Sans", sans-serif; font-weight: 700; color: var(--ink);
    font-size: 30px; line-height: 32px; text-transform: uppercase;
  }
</style>
</head>
<body>
  <svg class="hero" viewBox="0 0 1200 1060" xmlns="http://www.w3.org/2000/svg">
    <defs>
      <linearGradient id="photoTone" x1="0" y1="0" x2="1" y2="1">
        <stop offset="0" stop-color="#c9ccd2"/>
        <stop offset=".35" stop-color="#d9a58e"/>
        <stop offset=".6" stop-color="#4f8fc4"/>
        <stop offset="1" stop-color="#3d6a95"/>
      </linearGradient>
    </defs>
    <path d="M0 0 H1060 C1130 220 1110 560 900 800 C680 990 320 1030 0 1010 Z" fill="#ffffff"/>
    <path role="img" aria-label="Photo of a client lying face down on a treatment table under a blue towel"
          d="M0 0 H1030 C1080 240 1060 560 870 770 C660 950 320 990 0 975 Z" fill="url(#photoTone)"/>
  </svg>

  <div class="brand-seal">
    <div class="brand-name">Keel Street<span class="sub">Remedial Therapy</span></div>
  </div>

  <ul class="services">
    <li>Relaxation Massage</li>
    <li>Deep Tissue Massage</li>
    <li>Sports Massage</li>
    <li>Neuromuscular <span class="aside">(Trigger Point)</span> Therapy</li>
    <li>Postural Analysis</li>
    <li class="wrap">Musculoskeletal and Functional<br>Movement Screening</li>
    <li class="wrap">Therapeutic Stretching
      <span class="note">(Including Proprioceptive Neuromuscular<br>Facilitation and Muscle Energy Technique)</span></li>
  </ul>

  <div class="social">
    <div class="social-item"><span class="social-square"></span><span class="social-label">Chatterly</span></div>
    <div class="social-item"><span class="social-square"></span><span class="social-label">Snapframe</span></div>
  </div>

  <div class="custom-band">All sessions are customised to suit the needs of the client,<br>and may incorporate a variety of the above techniques.</div>

  <div class="price-box individual">
    <div class="price-head">Individual Sessions</div>
    <div class="price-body">
      <div class="price-row">30<span class="unit">min.</span><span class="dash">-</span><span class="cur">$</span>45</div>
      <div class="price-row">60<span class="unit">min.</span><span class="dash">-</span><span class="cur">$</span>85</div>
    </div>
  </div>

  <div class="price-box packages">
    <div class="price-head">Packages*</div>
    <div class="price-body">
      <div class="price-row">4<span class="times">x</span>30<span class="unit">min.</span><span class="dash">-</span><span class="cur">$</span>165</div>
      <div class="price-row">4<span class="times">x</span>60<span class="unit">min.</span><span class="dash">-</span><span class="cur">$</span>305</div>
    </div>
  </div>

  <p class="price-note">*(Packages valid for two months.<br>Pre-payment required)</p>

  <ul class="contact">
    <li>4/61 Tarrant Lane, Osborne Park WA 6017</li>
    <li><strong>0412 573 604</strong> · info@keelstreet.example.net</li>
  </ul>

  <div class="member">
    <span class="member-badge"></span>
    <span class="member-name">National<br>Remedial Therapists<br>Guild</span>
  </div>
</body>
</html>
```